I am looking for a stand-out cover that sings out to new parents. The category is very pastel with limited compelling covers that would make me want to buy a book. This book will be used often in the first 12 months of baby's life - so must be strong enough to sit on the bedside table or on the coffee table to inspire reading. It will be a popular gift - so needs to look credible, "pick-up-able" and loveable.

The Book Title is - The Cradle Compass to Infancy's Opening Seasons: Grounded, Research-Led Methods on Rest, Nourishment, Protection plus Growing Assurance
The Size is - 8.5 x 11 in
Book description to be provided to final design for inclusion
Some examples of book covers in this category attached. Thanks

```html
<!DOCTYPE html>
<html lang="en">
<head>
<meta charset="utf-8">
<title>The Cradle Compass to Infancy's Opening Seasons — Cover</title>
<link rel="stylesheet" href="https://fonts.googleapis.com/css2?family=Kaushan+Script&family=Poppins:wght@500;600&display=swap">
<style>
  :root {
    --backdrop: #8b8780;
    --paper: #f7f6f4;
    --ink: #6e6d6b;
    --blush: #f2d6d3;
    --skin-light: rgba(246, 222, 212, 0.95);
    --skin-mid: rgba(240, 200, 184, 0.85);
    --skin-fade: rgba(246, 222, 212, 0);
  }
  * { margin: 0; padding: 0; box-sizing: border-box; }
  html, body {
    width: 1200px;
    height: 2324px;
    overflow: hidden;
    background: var(--backdrop);
  }
  .cover {
    position: absolute;
    left: 100px;
    top: 515px;
    width: 1000px;
    height: 1294px;
    background: var(--paper);
    color: var(--ink);
    text-align: center;
  }
  .title {
    position: absolute;
    left: 0; right: 0;
    font-family: "Kaushan Script", cursive;
    font-weight: 400;
    line-height: 1;
  }
  .title-lead { top: 66px; font-size: 52px; }
  .title-main-1 { top: 124px; font-size: 132px; }
  .title-main-2 { top: 258px; font-size: 112px; }
  .title-minor-1 { top: 396px; font-size: 60px; }
  .title-minor-2 { top: 466px; font-size: 60px; }
  .decor { position: absolute; left: 0; top: 0; }
  .subtitle {
    position: absolute;
    left: 290px;
    width: 420px;
    top: 572px;
    font-family: "Poppins", sans-serif;
    font-weight: 600;
    font-size: 19px;
    line-height: 1.3;
  }
  .illustration {
    position: absolute;
    left: 262px;
    top: 700px;
    width: 476px;
    height: 444px;
    background:
      radial-gradient(ellipse 46% 40% at 64% 34%, var(--skin-light) 0%, var(--skin-fade) 100%),
      radial-gradient(ellipse 44% 46% at 40% 62%, var(--skin-mid) 0%, var(--skin-fade) 100%),
      radial-gradient(ellipse 30% 30% at 62% 80%, var(--skin-mid) 0%, var(--skin-fade) 100%);
  }
  .author {
    position: absolute;
    left: 0; right: 0;
    top: 1204px;
    font-family: "Poppins", sans-serif;
    font-weight: 600;
    font-size: 31px;
    letter-spacing: 0.32em;
  }
</style>
</head>
<body>
  <main class="cover">
    <svg class="decor" width="1000" height="1294" viewBox="0 0 1000 1294" aria-hidden="true">
      <g fill="var(--blush)">
        <path class="heart" d="M800 218c-6-22 22-34 34-16 10-18 40-8 34 14-5 18-34 36-34 36s-28-14-34-34z"/>
        <path class="heart" d="M165 345c-6-22 22-34 34-16 10-18 40-8 34 14-5 18-34 36-34 36s-28-14-34-34z"/>
      </g>
      <g stroke="var(--blush)" stroke-width="7" stroke-linecap="round">
        <line x1="280" y1="410" x2="335" y2="425"/>
        <line x1="262" y1="458" x2="320" y2="460"/>
        <line x1="280" y1="508" x2="335" y2="493"/>
        <line x1="720" y1="425" x2="775" y2="410"/>
        <line x1="680" y1="460" x2="738" y2="458"/>
        <line x1="665" y1="493" x2="720" y2="508"/>
      </g>
    </svg>
    <h1>
      <span class="title title-lead">The Cradle</span>
      <span class="title title-main-1">Compass</span>
      <span class="title title-main-2">to Infancy's</span>
      <span class="title title-minor-1">Opening</span>
      <span class="title title-minor-2">Seasons</span>
    </h1>
    <p class="subtitle">Grounded, Research-Led Methods on Rest, Nourishment, Protection plus Growing Assurance</p>
    <div class="illustration" role="img" aria-label="Soft watercolour illustration of a parent's hands gently cradling a baby's small hand"></div>
    <p class="author">AUTHOR NAME</p>
  </main>
</body>
</html>
```